Design a Banner for funny video website

Hi,

I need someone to design three(one from each dimension) 468x60, 300x250 and 125x125 banner ads. I am looking for something that is really eye-catching as well as simple. It should grab users attention at first glance and want to know more about whats the ad all about.

You are designing the ad for quiplark.net. You should review the site to get a feeling about what you need to achieve.

Thank you..

```html
<!DOCTYPE html>
<html lang="en">
<head>
<meta charset="utf-8">
<title>quiplark.net banner set</title>
<link rel="stylesheet" href="https://fonts.googleapis.com/css2?family=Anton&family=Oswald:wght@600;700&family=Archivo+Black&family=Open+Sans:wght@700&display=swap">
<style>
  :root {
    --board: #2a2a2a;
    --board-light: #3a3a3a;
    --paper: #ffffff;
    --ink: #1c1c1c;
    --red: #d0141c;
    --red-deep: #8e0a10;
    --button-top: #ffffff;
    --button-bottom: #d9d9d9;
    --photo-skin: #d8b49a;
    --photo-shade: #8a6a58;
    --photo-shirt: #232323;
    --label: #ffffff;
  }
  * { margin: 0; padding: 0; box-sizing: border-box; }
  html, body { width: 1200px; height: 800px; overflow: hidden; }
  body {
    position: relative;
    background: radial-gradient(ellipse at 50% 40%, var(--board-light), var(--board) 75%);
    font-family: "Open Sans", Arial, sans-serif;
  }
  .board-title {
    position: absolute; left: 0; width: 100%; top: 20px;
    padding-left: 166px;
    text-align: center;
    color: var(--label);
    font-size: 31px; font-weight: 700; letter-spacing: 1.5px;
  }
  .size-label {
    position: absolute;
    color: var(--label);
    font-size: 15px; font-weight: 700;
    transform: translateX(-50%);
  }
  .banner {
    position: absolute;
    background: var(--paper);
    overflow: hidden;
  }
  .banner .wedge { position: absolute; inset: 0; width: 100%; height: 100%; }
  .photo {
    position: absolute;
    background: linear-gradient(180deg, var(--photo-shade) 0%, var(--photo-skin) 35%, var(--photo-skin) 62%, var(--photo-shirt) 82%);
    border-radius: 45% 45% 8% 8% / 35% 35% 4% 4%;
  }
  .headline {
    position: absolute;
    font-family: "Anton", Impact, sans-serif;
    color: var(--ink);
    text-transform: uppercase;
    line-height: 1;
    white-space: nowrap;
  }
  .cta-button {
    position: absolute;
    display: flex; align-items: center; justify-content: center;
    background: linear-gradient(180deg, var(--button-top), var(--button-bottom));
    font-family: "Oswald", "Arial Narrow", sans-serif; font-weight: 700;
    color: var(--ink);
    white-space: nowrap;
  }
  .cta-sub {
    position: absolute;
    font-family: "Archivo Black", Arial, sans-serif;
    color: var(--paper);
    white-space: nowrap;
    text-align: center;
  }

  /* 468x60 leaderboard */
  .banner--leader { left: 66px; top: 139px; width: 748px; height: 96px; }
  .banner--leader .photo { left: 10px; top: 4px; width: 62px; height: 92px; }
  .banner--leader .headline { left: 108px; top: 27px; font-size: 38px; letter-spacing: 0.5px; }
  .banner--leader .cta-button { left: 518px; top: 11px; width: 197px; height: 50px; border-radius: 16px; font-size: 30px; }
  .banner--leader .cta-sub { left: 518px; top: 66px; width: 197px; font-size: 19px; letter-spacing: 2px; }

  /* 300x250 medium rectangle */
  .banner--rect { left: 66px; top: 344px; width: 480px; height: 400px; }
  .banner--rect .headline { left: 10px; font-size: 98px; letter-spacing: 1px; }
  .banner--rect .headline--one { top: 12px; }
  .banner--rect .headline--two { top: 110px; }
  .banner--rect .photo { left: 30px; top: 216px; width: 136px; height: 184px; }
  .banner--rect .cta-button { left: 266px; top: 267px; width: 208px; height: 80px; border-radius: 28px; font-size: 38px; }
  .banner--rect .cta-sub { left: 262px; top: 353px; width: 212px; font-size: 27px; letter-spacing: 2.5px; }

  /* 125x125 square */
  .banner--square { left: 586px; top: 346px; width: 200px; height: 200px; }
  .banner--square .headline--one { left: 5px; top: 4px; width: 190px; font-size: 52px; letter-spacing: 4px; }
  .banner--square .headline--two { left: 5px; top: 60px; width: 190px; font-size: 32px; letter-spacing: 2.5px; }
  .banner--square .photo { left: 6px; top: 96px; width: 80px; height: 104px; }
  .banner--square .cta-button {
    left: 88px; top: 112px; width: 106px; height: 38px; border-radius: 19px;
    background: linear-gradient(180deg, var(--red), var(--red-deep));
    border: 2px solid var(--paper); box-shadow: 0 0 0 1px #bbb;
    color: var(--paper); font-size: 17px;
  }
  .banner--square .cta-sub { left: 88px; top: 154px; width: 106px; color: var(--ink); font-size: 13px; letter-spacing: 1px; }
</style>
</head>
<body>
  <h1 class="board-title">Please read description to see animation</h1>

  <span class="size-label" style="left:451px; top:98px;">468x60</span>
  <section class="banner banner--leader" aria-label="quiplark.net 468 by 60 banner">
    <svg class="wedge" viewBox="0 0 748 96" preserveAspectRatio="none" aria-hidden="true">
      <defs>
        <linearGradient id="leader-red" x1="0" y1="0" x2="0" y2="1">
          <stop offset="0" stop-color="#e3161f"/>
          <stop offset="1" stop-color="#9c0b11"/>
        </linearGradient>
      </defs>
      <polygon points="518,0 748,0 748,96 387,96" fill="url(#leader-red)"/>
    </svg>
    <div class="photo" role="img" aria-label="Photo of a laughing man"></div>
    <p class="headline">What’s so funny?</p>
    <div class="cta-button">CLICK HERE</div>
    <p class="cta-sub">TO FIND OUT</p>
  </section>

  <span class="size-label" style="left:304px; top:306px;">300x250</span>
  <section class="banner banner--rect" aria-label="quiplark.net 300 by 250 banner">
    <svg class="wedge" viewBox="0 0 480 400" preserveAspectRatio="none" aria-hidden="true">
      <defs>
        <linearGradient id="rect-red" x1="0" y1="0" x2="0" y2="1">
          <stop offset="0" stop-color="#e3161f"/>
          <stop offset="1" stop-color="#9c0b11"/>
        </linearGradient>
      </defs>
      <polygon points="480,0 480,400 173,400" fill="url(#rect-red)"/>
    </svg>
    <p class="headline headline--one">What’s so</p>
    <p class="headline headline--two">Funny?</p>
    <div class="photo" role="img" aria-label="Photo of a man laughing out loud"></div>
    <div class="cta-button">CLICK HERE</div>
    <p class="cta-sub">TO FIND OUT</p>
  </section>

  <span class="size-label" style="left:685px; top:306px;">125x125</span>
  <section class="banner banner--square" aria-label="quiplark.net 125 by 125 banner">
    <p class="headline headline--one">What’s</p>
    <p class="headline headline--two">So funny?</p>
    <div class="photo" role="img" aria-label="Photo of a man laughing"></div>
    <div class="cta-button">CLICK HERE</div>
    <p class="cta-sub">TO FIND OUT</p>
  </section>
</body>
</html>
```